New innovative Legal start-up looking for letterhead and business card template

Using our existing logo, colours and font we need a simple, professional, accessible (easy to read), and consistent letterhead and business card design template. Letterhead will be printed in house so heavy colour is not preferred (though some colour is acceptable). Letter sis is US Letter (21.59 cm x 27.94cm) and business card is standard size (3.5"x 2")Logo Proof sheet is attached. Logo designs can be found here https://www.filquarry.example/sh/tz4kp9wq2lmn83r/QXR7HV2bLsNpKfZ41wdYeuCmo?dl=0

```html
<!DOCTYPE html>
<html lang="en">
<head>
<meta charset="utf-8">
<title>Veridan Legal Access – Stationery</title>
<link href="https://fonts.googleapis.com/css2?family=Lato:wght@400;700&display=swap" rel="stylesheet">
<style>
  :root{
    --backdrop:#2e2e2e;
    --paper:#ffffff;
    --ink:#7a7a7a;
    --ink-dark:#5c5c5c;
    --teal:#0aa59a;
    --navy:#232846;
    --orange:#f47b20;
    --card-grey:#8e8e8e;
  }
  *{margin:0;padding:0;box-sizing:border-box}
  html,body{width:1189px;height:1200px;overflow:hidden;background:var(--backdrop);font-family:'Lato',sans-serif;color:var(--ink)}
  .canvas{position:relative;width:1189px;height:1200px}

  .sheet{position:absolute;background:var(--paper)}
  .letterhead{top:100px;width:508px;height:657px}
  .letterhead--front{left:72px}
  .letterhead--back{left:608px}

  .brand-bands{position:absolute;left:0;right:0;bottom:0;height:6px;display:flex}
  .brand-bands span{flex:1}
  .band-teal{background:var(--teal)}
  .band-navy{background:var(--navy)}
  .band-orange{background:var(--orange)}

  .brand{position:absolute;display:flex;align-items:center;gap:8px}
  .brand-disc{border:2px solid var(--ink);border-radius:50%}
  .brand-name{font-weight:400;color:var(--ink);letter-spacing:.5px;line-height:1}

  .letterhead .brand{left:42px;top:43px}
  .letterhead .brand-disc{width:50px;height:50px}
  .letterhead .brand-name{font-size:19px}

  .lh-contact{position:absolute;left:348px;top:39px;padding-left:11px;border-left:1.5px solid var(--orange);font-size:8.5px;line-height:11px;color:var(--ink)}
  .lh-contact .address{margin-bottom:4px}

  .contact-line{display:flex;align-items:center;gap:3px}
  .icon{flex:none}

  .card{top:862px;width:353px;height:201px}
  .card--back{left:70px;background:var(--card-grey);overflow:hidden}
  .card-pattern{position:absolute;inset:0;background:radial-gradient(circle at 50% 50%,#999 0%,#8a8a8a 100%)}
  .card--back .brand{left:68px;top:65px;gap:12px}
  .card--back .brand-disc{width:72px;height:72px;border:3px solid #fff}
  .card--back .brand-name{color:#fff;font-size:24px}

  .card--front{left:460px;top:863px;width:352px;height:199px}
  .card--front .brand{left:18px;top:23px}
  .card--front .brand-disc{width:54px;height:54px}
  .card--front .brand-name{font-size:19px}

  .holder{position:absolute;left:18px;top:105px}
  .holder-name{font-size:12px;color:var(--ink-dark);letter-spacing:.2px;line-height:13px}
  .holder-role{font-size:10px;color:var(--orange);line-height:11px}
  .card-rule{position:absolute;left:18px;right:20px;top:132px;height:1px;background:var(--orange)}
  .card-contact{position:absolute;left:18px;top:145px;font-size:9.5px;line-height:12.5px;color:var(--ink)}
  .card-address{position:absolute;right:20px;top:157px;font-size:9.5px;line-height:12px;text-align:right;color:var(--ink)}
  .card--front .brand-bands{height:7px}
</style>
</head>
<body>
<main class="canvas">

  <section class="sheet letterhead letterhead--front" aria-label="Letterhead, first page">
    <div class="brand">
      <span class="brand-disc"></span>
      <span class="brand-name">VERIDAN LEGAL ACCESS</span>
    </div>
    <address class="lh-contact" style="font-style:normal">
      <div class="address">PO Box 418 Harlow Lane,<br>7 Bristow Road, USA</div>
      <div class="contact-line">
        <svg class="icon" width="8" height="8" viewBox="0 0 8 8"><circle cx="4" cy="4" r="3.5" fill="none" stroke="#0aa59a"/><rect x="2.8" y="2" width="2.4" height="4" rx=".4" fill="#0aa59a"/></svg>(01) 4820 1735
      </div>
      <div class="contact-line">
        <svg class="icon" width="8" height="8" viewBox="0 0 8 8"><circle cx="4" cy="4" r="3.5" fill="none" stroke="#232846"/><rect x="2" y="2.8" width="4" height="2.6" fill="#232846"/></svg>hello@veridanlegal.example
      </div>
      <div class="contact-line">
        <svg class="icon" width="8" height="8" viewBox="0 0 8 8"><circle cx="4" cy="4" r="3.5" fill="none" stroke="#f47b20"/><circle cx="4" cy="4" r="2" fill="#f47b20"/></svg>www.veridanlegal.example
      </div>
    </address>
    <div class="brand-bands"><span class="band-teal"></span><span class="band-navy"></span><span class="band-orange"></span></div>
  </section>

  <section class="sheet letterhead letterhead--back" aria-label="Letterhead, continuation page">
    <div class="brand-bands"><span class="band-teal"></span><span class="band-navy"></span><span class="band-orange"></span></div>
  </section>

  <section class="sheet card card--back" aria-label="Business card, back">
    <div class="card-pattern" role="img" aria-label="Grey repeating brand pattern background"></div>
    <div class="brand">
      <span class="brand-disc"></span>
      <span class="brand-name">VERIDAN</span>
    </div>
  </section>

  <section class="sheet card card--front" aria-label="Business card, front">
    <div class="brand">
      <span class="brand-disc"></span>
      <span class="brand-name">VERIDAN LEGAL ACCESS</span>
    </div>
    <div class="holder">
      <div class="holder-name">NORA FELD</div>
      <div class="holder-role">Manager</div>
    </div>
    <div class="card-rule"></div>
    <div class="card-contact">
      <div class="contact-line">
        <svg class="icon" width="10" height="10" viewBox="0 0 8 8"><circle cx="4" cy="4" r="3.5" fill="none" stroke="#0aa59a"/><rect x="2.8" y="2" width="2.4" height="4" rx=".4" fill="#0aa59a"/></svg>(01) 4820 1735
      </div>
      <div class="contact-line">
        <svg class="icon" width="10" height="10" viewBox="0 0 8 8"><circle cx="4" cy="4" r="3.5" fill="none" stroke="#232846"/><rect x="2" y="2.8" width="4" height="2.6" fill="#232846"/></svg>hello@veridanlegal.example
      </div>
      <div class="contact-line">
        <svg class="icon" width="10" height="10" viewBox="0 0 8 8"><circle cx="4" cy="4" r="3.5" fill="none" stroke="#f47b20"/><circle cx="4" cy="4" r="2" fill="#f47b20"/></svg>www.veridanlegal.example
      </div>
    </div>
    <div class="card-address">PO Box 418 Harlow Lane,<br>7 Bristow Road, USA</div>
    <div class="brand-bands"><span class="band-teal"></span><span class="band-navy"></span><span class="band-orange"></span></div>
  </section>

</main>
</body>
</html>
```